Corvel Ridge New Website Design

We just changed our logo (thank you PlanHarbor) and company name change from Corvel Ridge Machining to Corvel Ridge Manufacturing. We do CNC Swiss screw machining and multi-axis machines. We make parts for many industries. We make large quantity production parts as well small R&D quantities. You can look at our current (outdated) website: http://www.corvelridgemachining.example to see what we do. We would like a WordPress site, including contact form for "request for quote" . We would also like it to be mobile friendly, and the ability to maintain it ourselves after it is finished I have included our new logo and fonts for references. We would like our site to convey the feeling of precision, capability, and trust worthiness with a very modern look. The new website address is www.corvelridge-mfg.example

Coding

Coded - Design and coding required

Number of Pages Required

5+ page

Font styles to use
Serif
Sans Serif
Other font styles liked:
• fronts included, not sure if they work

Colors

Designer to choose colors to be used in the design.

Requirements
Must have
• Contact Info, request for quote field

```html
<!DOCTYPE html>
<html lang="en">
<head>
<meta charset="utf-8">
<title>Corvel Ridge Manufacturing</title>
<link href="https://fonts.googleapis.com/css2?family=Montserrat:wght@300;400;500;600;700&display=swap" rel="stylesheet">
<style>
:root{
  --blue:#2a4a97;
  --blue-dark:#1c3d8f;
  --green:#5ccf22;
  --ink:#2c2c2c;
  --muted:#555;
  --pale:#e6edfb;
  --white:#fff;
  --black:#000;
}
*{margin:0;padding:0;box-sizing:border-box}
html,body{width:1200px;height:3764px;overflow:hidden}
body{font-family:'Montserrat',sans-serif;color:var(--ink);background:var(--white);position:relative}
.abs{position:absolute}
.btn{display:inline-flex;align-items:center;justify-content:center;background:var(--green);color:var(--white);font-weight:600;border-radius:30px;text-transform:uppercase;font-size:14px}

/* header */
.header{top:0;left:0;width:1200px;height:129px}
.address{left:107px;top:48px;font-size:11px;line-height:16px;color:var(--muted);display:flex;gap:8px}
.brand{left:0;width:1200px;top:40px;text-align:center}
.brand-name{font-size:30px;font-weight:600;color:var(--blue);letter-spacing:1px;line-height:34px}
.brand-sub{font-size:10px;letter-spacing:2px;color:var(--blue);margin-top:2px}
.phone{left:800px;top:57px;font-size:12px;color:var(--muted);display:flex;gap:10px;align-items:center}
.header .btn{left:937px;top:44px;width:154px;height:43px;font-size:12px}

.nav{top:129px;left:0;width:1200px;height:57px;background:var(--blue);color:var(--white)}
.nav ul{list-style:none;display:flex;position:absolute;left:108px;top:21px;font-size:12px;font-weight:500}
.nav li{margin-right:40px}
.nav .search{position:absolute;left:1073px;top:20px}

/* hero */
.hero{top:186px;left:0;width:1200px;height:574px;background:linear-gradient(90deg,#f4f5f7 0%,#e9ecef 45%,#b9c0c8 75%,#6d7783 100%)}
.hero-title{left:107px;top:298px;font-size:50px;font-weight:400;color:var(--blue);line-height:60px;letter-spacing:1px}
.hero-text{left:107px;top:432px;font-size:15px;line-height:25px;color:var(--ink)}
.hero .btn{left:107px;top:500px}
.hero-btn{left:107px;top:500px;width:154px;height:43px}
.arrow{width:30px;height:50px}

/* industries */
.industries{top:760px;left:0;width:1200px;height:678px;background:linear-gradient(90deg,#1f3f91,#2c4a96)}
.section-title{width:1200px;left:0;text-align:center;font-size:32px;font-weight:400;letter-spacing:1px}
.industry{width:220px;text-align:center;color:var(--white)}
.industry svg{display:block;margin:0 auto}
.industry h3{font-size:14px;font-weight:700;margin-top:14px}
.industry p{font-size:11px;line-height:15px;margin-top:20px}

/* less */
.less-title{left:107px;top:1564px;font-size:30px;font-weight:400;color:var(--blue);letter-spacing:.5px}
.less-text{left:107px;top:1612px;width:460px;font-size:14px;line-height:25px;color:var(--ink)}
.less-photo{left:604px;top:1527px;width:596px;height:426px;background:linear-gradient(135deg,#eef1f4,#c9ced6 50%,#8c6e56)}

/* quote */
.quote{top:2033px;left:0;width:1200px;height:630px;background:var(--pale)}
.field{background:var(--white);font-size:11px;color:#888;padding:14px 14px}
.send{left:282px;top:2536px;width:657px;height:49px;font-size:16px;letter-spacing:4px;border-radius:30px}

/* testimonial */
.quote-mark{font-size:170px;font-weight:700;color:#d4d4d4;line-height:1}
.dot{width:11px;height:11px;border-radius:50%;background:#ddd}

/* cta */
.cta{top:3179px;left:0;width:1200px;height:130px;background:linear-gradient(90deg,#2a4a97,#1c3b8e)}

/* footer */
.footer{top:3309px;left:0;width:1200px;height:455px;background:var(--black);color:var(--white)}
.footer-links{width:1200px;left:0;text-align:center;font-size:12px}
.footer-links span{margin:0 11px}
</style>
</head>
<body>

<header class="header abs">
  <div class="address abs">
    <svg width="10" height="14" viewBox="0 0 10 14"><path d="M5 0C2.2 0 0 2.2 0 5c0 3.5 5 9 5 9s5-5.5 5-9C10 2.2 7.8 0 5 0z" fill="#5ccf22"/><circle cx="5" cy="5" r="2" fill="#fff"/></svg>
    <div>48 Harlow Lane, Suite 210<br>Building No. 7</div>
  </div>
  <div class="brand abs">
    <div class="brand-name">CORVEL RIDGE</div>
    <div class="brand-sub">MANUFACTURING</div>
  </div>
  <div class="phone abs">
    <svg width="14" height="14" viewBox="0 0 24 24"><path d="M6.6 10.8c1.4 2.8 3.8 5.1 6.6 6.6l2.2-2.2c.3-.3.7-.4 1-.2 1.1.4 2.3.6 3.6.6.6 0 1 .4 1 1V20c0 .6-.4 1-1 1C10.6 21 3 13.4 3 4c0-.6.4-1 1-1h3.5c.6 0 1 .4 1 1 0 1.3.2 2.5.6 3.6.1.3 0 .7-.2 1L6.6 10.8z" fill="#5ccf22"/></svg>
    555-014-2738
  </div>
  <a class="btn abs">Request A Quote</a>
</header>

<nav class="nav abs">
  <ul>
    <li>SERVICES</li><li>EQUIPMENT</li><li>QUALITY</li><li>OUR WORK</li><li>ABOUT US</li><li>CONTACT US</li><li>SITE MAP</li>
  </ul>
  <svg class="search" width="16" height="16" viewBox="0 0 16 16"><circle cx="6.5" cy="6.5" r="5" stroke="#fff" stroke-width="2" fill="none"/><path d="M10 10l4.5 4.5" stroke="#fff" stroke-width="2"/></svg>
</nav>

<section class="hero abs" role="img" aria-label="Team meeting with a presenter at a whiteboard in a bright office"></section>
<h1 class="hero-title abs">MAXIMIZE THE VALUE &amp;<br>QUALITY IN YOUR PRODUCT</h1>
<p class="hero-text abs">CSpecializing in precision, Corvel Ridge will provide you<br>with superior products, at affordable prices.</p>
<a class="btn abs hero-btn">Learn More</a>
<svg class="arrow abs" style="left:32px;top:425px" viewBox="0 0 30 50"><path d="M26 2L4 25l22 23" stroke="#aaa" stroke-width="2" fill="none"/></svg>
<svg class="arrow abs" style="left:1138px;top:425px" viewBox="0 0 30 50"><path d="M4 2l22 23L4 48" stroke="#ddd" stroke-width="2" fill="none"/></svg>

<section class="industries abs">
  <h2 class="section-title abs" style="top:852px;color:#fff;position:fixed"></h2>
</section>
<h2 class="section-title abs" style="top:852px;color:#fff">INDUSTRIES SERVED</h2>

<div class="industry abs" style="left:92px;top:960px">
  <svg width="40" height="40" viewBox="0 0 40 40" fill="none" stroke="#5ccf22" stroke-width="2"><path d="M6 34L34 6M14 22l-8-2 4-4 10 2M18 26l2 8 4-4-2-10"/></svg>
  <h3>Aerospace</h3><p>Lorem ipsum dolor sit amet,<br>consectetur adipisicing elit, sed<br>do eiusmod tempor incididunt</p>
</div>
<div class="industry abs" style="left:355px;top:960px">
  <svg width="40" height="40" viewBox="0 0 40 40" fill="none" stroke="#5ccf22" stroke-width="2"><rect x="5" y="16" width="30" height="14" rx="3"/><path d="M10 16l4-8h12l4 8"/><circle cx="12" cy="32" r="3"/><circle cx="28" cy="32" r="3"/></svg>
  <h3>Automotive</h3><p>Lorem ipsum dolor sit amet,<br>consectetur adipisicing elit, sed<br>do eiusmod tempor incididunt</p>
</div>
<div class="industry abs" style="left:619px;top:960px">
  <svg width="40" height="40" viewBox="0 0 40 40" fill="none" stroke="#5ccf22" stroke-width="2"><rect x="6" y="6" width="28" height="20" rx="2"/><path d="M16 26v6M24 26v6M10 34h20"/></svg>
  <h3>Computer</h3><p>Lorem ipsum dolor sit amet,<br>consectetur adipisicing elit, sed<br>do eiusmod tempor incididunt</p>
</div>
<div class="industry abs" style="left:882px;top:960px">
  <svg width="40" height="40" viewBox="0 0 40 40" fill="none" stroke="#5ccf22" stroke-width="2"><path d="M10 6c-5 0-6 8-3 14 2 4 2 14 6 14s3-8 7-8 3 8 7 8 4-10 6-14c3-6 2-14-3-14-4 0-6 2-10 2S14 6 10 6z"/></svg>
  <h3>Dental</h3><p>Lorem ipsum dolor sit amet,<br>consectetur adipisicing elit, sed<br>do eiusmod tempor incididunt</p>
</div>
<div class="industry abs" style="left:226px;top:1196px">
  <svg width="40" height="40" viewBox="0 0 40 40" fill="none" stroke="#5ccf22" stroke-width="2"><rect x="12" y="12" width="16" height="16"/><path d="M16 4v8M24 4v8M16 28v8M24 28v8M4 16h8M4 24h8M28 16h8M28 24h8"/></svg>
  <h3>Electronics</h3><p>Lorem ipsum dolor sit amet,<br>consectetur adipisicing elit, sed<br>do eiusmod tempor incididunt</p>
</div>
<div class="industry abs" style="left:489px;top:1196px">
  <svg width="40" height="40" viewBox="0 0 40 40" fill="none" stroke="#5ccf22" stroke-width="2"><circle cx="20" cy="8" r="3"/><path d="M20 11v24M12 18h16M8 26c2 6 7 9 12 9s10-3 12-9"/></svg>
  <h3>Marine</h3><p>Lorem ipsum dolor sit amet,<br>consectetur adipisicing elit, sed<br>do eiusmod tempor incididunt</p>
</div>
<div class="industry abs" style="left:754px;top:1196px">
  <svg width="40" height="40" viewBox="0 0 40 40" fill="none" stroke="#5ccf22" stroke-width="2"><path d="M20 34L7 21C2 16 5 7 12 7c4 0 6 3 8 5 2-2 4-5 8-5 7 0 10 9 5 14z"/><path d="M8 20h8l2-4 4 8 2-4h8"/></svg>
  <h3>Medical</h3><p>Lorem ipsum dolor sit amet,<br>consectetur adipisicing elit, sed<br>do eiusmod tempor incididunt</p>
</div>

<h2 class="less-title abs">WHEN LESS IS MORE</h2>
<div class="less-text abs">
  <p>Corvel Ridge Machining Company is a high quality machining resource providing friendly service, fast turnaround times, and engineering expertise, at competitive pricing.&nbsp; With almost 20 years of experience in the industry, Corvel Ridge utilizes certified state of the art equipment partnered with top professionals to maximize the value and quality in your product.</p>
  <p style="margin-top:18px">CSpecializing in precision, Corvel Ridge will provide you<br>with superior products, at affordable prices.</p>
</div>
<a class="btn abs" style="left:107px;top:1859px;width:154px;height:43px">Learn More</a>
<div class="less-photo abs" role="img" aria-label="Colleagues collaborating around a laptop at an office table"></div>

<section class="quote abs"></section>
<h2 class="section-title abs" style="top:2104px;color:var(--blue)">REQUEST A QUOTE</h2>
<p class="abs" style="left:0;width:1200px;top:2178px;text-align:center;font-size:13px;line-height:25px;color:var(--muted)">Lorem ipsum dolor sit amet, consectetur adipisicing elit, sed do eiusmod tempor incididunt ut<br>labore et dolore magna aliqua. Ut enim ad minim veniam.</p>
<div class="field abs" style="left:282px;top:2265px;width:322px;height:42px">Name</div>
<div class="field abs" style="left:620px;top:2265px;width:318px;height:42px">Company</div>
<div class="field abs" style="left:282px;top:2328px;width:656px;height:42px">Email</div>
<div class="field abs" style="left:282px;top:2391px;width:656px;height:127px">Request</div>
<a class="btn abs send">Send</a>

<h2 class="section-title abs" style="top:2756px;color:var(--blue)">TESTIMONIAL</h2>
<div class="quote-mark abs" style="left:145px;top:2790px">&ldquo;</div>
<div class="quote-mark abs" style="left:970px;top:2790px">&rdquo;</div>
<p class="abs" style="left:0;width:1200px;top:2838px;text-align:center;font-size:16px;line-height:33px;color:var(--ink)">I love working with engineers. Finding ways to make their parts less expensive is a<br>puzzle I never get tired of solving.</p>
<div class="abs" role="img" aria-label="Portrait of the client giving the testimonial" style="left:556px;top:2930px;width:88px;height:88px;background:linear-gradient(180deg,#e4e6e9,#9aa6b4)"></div>
<p class="abs" style="left:0;width:1200px;top:3042px;text-align:center;font-size:19px;color:var(--blue);font-weight:500">Daniel Verhoef</p>
<div class="abs" style="left:559px;top:3121px;display:flex;gap:6px">
  <div class="dot" style="background:var(--green)"></div><div class="dot"></div><div class="dot"></div><div class="dot"></div><div class="dot"></div>
</div>
<svg class="arrow abs" style="left:32px;top:2879px" viewBox="0 0 30 50"><path d="M26 2L4 25l22 23" stroke="#888" stroke-width="2" fill="none"/></svg>
<svg class="arrow abs" style="left:1138px;top:2879px" viewBox="0 0 30 50"><path d="M4 2l22 23L4 48" stroke="#888" stroke-width="2" fill="none"/></svg>

<section class="cta abs"></section>
<p class="abs" style="left:314px;top:3231px;font-size:20px;color:#fff">For Any Solution We Are Available here.</p>
<a class="btn abs" style="left:730px;top:3222px;width:154px;height:43px">Call Now</a>

<footer class="footer abs"></footer>
<div class="brand abs" style="top:3410px">
  <div class="brand-name" style="color:#fff">CORVEL RIDGE</div>
  <div class="brand-sub" style="color:#fff">MANUFACTURING</div>
</div>
<div class="footer-links abs" style="top:3512px;color:#fff">
  <span>About Us</span><span>Request A Quote</span><span>Testimonials</span><span>Equipment</span><span>Services</span>
</div>
<div class="abs" style="left:514px;top:3556px;display:flex;gap:35px">
  <div style="width:14px;height:14px;border-radius:50%;background:#fff"></div>
  <div style="width:14px;height:14px;border-radius:50%;background:#fff"></div>
  <div style="width:14px;height:14px;border-radius:50%;background:#fff"></div>
  <div style="width:14px;height:14px;border-radius:50%;background:#fff"></div>
</div>
<div class="abs" style="left:535px;top:3609px;width:64px;height:48px;background:#e9731f"></div>
<div class="abs" style="left:618px;top:3609px;width:48px;height:48px;border-radius:50%;background:#cfcfcf"></div>
<div class="abs" style="left:129px;top:3670px;width:943px;height:1px;background:#333"></div>
<p class="abs" style="left:0;width:1200px;top:3710px;text-align:center;font-size:12px;color:#fff">&copy; Copyright Corvel Ridge Manufacturing. All rights reserved</p>

</body>
</html>
```